label design needed for beef product

i need a simple nice packaging design like these
https://www.shopquarry.test/Jolt-Pantry-Gelatin-Natural-Powder/dp/K742RTQ915/ref=sr_1_3_a_it?ie=UTF8&qid=1494282127&sr=8-3&keywords=beef+gelatin+powder

My company name is TIRO
See logo
https://www.shopquarry.test/Vitamin-Hyaluronic-Nutrient-Lighten-Circles/dp/K58ZP37QLX/ref=sr_1_3_a_it?ie=UTF8&qid=1494282386&sr=8-3&keywords=tiro&th=1

i must have the same logo on the label design ,
see attached for the front wording and the back

the facts or the same as the now

Target Market(s)

Shopquarry,

Industry/Entity Type

Health And Wellness

Font styles to use
Serif
Sans Serif

Colors

Designer to choose colors to be used in the design.

Requirements
Must have
• the logo like it is on the following link
• https://www.shopquarry.test/Vitamin-Hyaluronic-Nutrient-Lighten-Circles/dp/K58ZP37QLX/ref=sr_1_3_a_it?ie=UTF8&qid=1494282386&sr=8-3&keywords=tiro&th=1
• I need a professional nice listing
Nice to have
• a nice background the packaging size will be the same as now see below
• https://www.shopquarry.test/Jolt-Pantry-Gelatin-Natural-Powder/dp/K742RTQ915/ref=sr_1_3_a_it?ie=UTF8&qid=1494282491&sr=8-3&keywords=beef+gelatin
• i like that design but i want much more professional to it
Should not have
• will discuss

```html
<!DOCTYPE html>
<html lang="en">
<head>
<meta charset="utf-8">
<title>TIRO Unflavored Beef Gelatin Powder – Label</title>
<link href="https://fonts.googleapis.com/css2?family=Lato:wght@400;700&family=Montserrat:wght@300;400&display=swap" rel="stylesheet">
<style>
  :root {
    --backdrop: #1c1c1c;
    --label: #ffffff;
    --plum: #6e2f8f;
    --plum-light: #9a5aa8;
    --mauve: #a8669e;
    --mauve-soft: #c9a0c4;
    --ink: #333333;
    --ink-dark: #111111;
  }
  * { margin: 0; padding: 0; box-sizing: border-box; }
  html, body {
    width: 1200px; height: 999px; overflow: hidden;
    background: var(--backdrop);
  }
  .label {
    position: absolute; left: 275px; top: 60px;
    width: 650px; height: 880px;
    background: var(--label);
    font-family: "Lato", sans-serif;
  }
  .brand {
    position: absolute; top: 78px; left: 0; width: 100%;
    display: flex; justify-content: center; align-items: center; gap: 28px;
  }
  .brand-dot {
    width: 86px; height: 86px; border-radius: 50%;
    border: 5px solid var(--mauve-soft);
  }
  .brand-name {
    font-family: "Lato", sans-serif; font-weight: 700;
    font-size: 82px; color: var(--mauve); letter-spacing: 1px; line-height: 1;
  }
  .band { position: absolute; left: 0; top: 220px; width: 650px; height: 350px; }
  .band-text { position: absolute; left: 0; width: 100%; text-align: center; color: #fff; }
  .band-kicker {
    top: 290px; font-family: "Montserrat", sans-serif; font-weight: 400;
    font-size: 30px; letter-spacing: 2px;
  }
  .band-title {
    top: 330px; font-family: "Montserrat", sans-serif; font-weight: 400;
    font-size: 124px; line-height: 1; letter-spacing: -2px;
  }
  .band-sub {
    top: 462px; font-family: "Montserrat", sans-serif; font-weight: 300;
    font-size: 44px; letter-spacing: 9px;
  }
  .claims {
    position: absolute; top: 580px; left: 115px; width: 420px;
    border-top: 1.5px solid var(--mauve-soft);
    border-bottom: 1.5px solid var(--mauve-soft);
    padding: 8px 0; text-align: center;
    font-size: 23px; line-height: 30px; color: var(--ink);
  }
  .callout {
    position: absolute; font-weight: 700; font-size: 26px; line-height: 30px;
    color: var(--mauve);
  }
  .callout-protein { left: 40px; top: 720px; }
  .callout-pure { right: 40px; top: 705px; text-align: right; }
  .net-weight {
    position: absolute; top: 838px; width: 100%; text-align: center;
    font-weight: 700; font-size: 23px; color: var(--ink-dark);
  }
</style>
</head>
<body>
  <main class="label">
    <div class="brand">
      <span class="brand-dot"></span>
      <span class="brand-name">tiro</span>
    </div>

    <svg class="band" viewBox="0 0 650 350" aria-hidden="true">
      <defs>
        <radialGradient id="bandFill" cx="50%" cy="50%" r="60%">
          <stop offset="0" stop-color="var(--plum-light)"/>
          <stop offset="1" stop-color="var(--plum)"/>
        </radialGradient>
      </defs>
      <path d="M0 0 Q325 70 650 0 L650 345 Q325 285 0 345 Z" fill="url(#bandFill)"/>
      <path d="M0 345 Q325 285 650 345" fill="none" stroke="var(--mauve-soft)" stroke-width="3"/>
    </svg>

    <p class="band-text band-kicker">UNFLAVORED BEEF</p>
    <h1 class="band-text band-title">GELATIN</h1>
    <p class="band-text band-sub">powder</p>

    <ul class="claims" style="list-style:none">
      <li>Stimulates Collagen production</li>
      <li>Reduces fine lines and wrinkles</li>
      <li>Strengthens hair, nails &amp; teeth</li>
    </ul>

    <p class="callout callout-protein">Excellent Source<br>of Protein!</p>
    <p class="callout callout-pure">100%<br>Pure Natural<br>Collagen Protein</p>

    <p class="net-weight">Net Wt. 1 Lb (454 g)</p>
  </main>
</body>
</html>
```